Calendar Ad / Flyer

Our law firm needs a calendar ad to place in a local calendar.
THE DEADLINE IS THIS THURSDAY 06/28/2018.

Attached is the ad used in last years calendar. A few notes on this...
**. This is by no means the model to follow.
Please be creative and do what makes more sense marketing wise.
1. Need to update the color scheme which corresponds to the new website at marvolinlegal.com
2. The "MARVOLIN LAW | SHAPING FAITH WITH RESULTS" should be put at the top and made larger
3. "KNOWN AND TRUSTED IN OUR COMMUNITY FOR OVER 21 YEARS" should be changed to "KNOWN AND TRUSTED IN OUR COMMUNITY FOR OVER 22 YEARS"
4. "Gordon R. Marvolin, Esq." should be made larger and better positioned.
5. Under the list of practices, it should be changed to have:
"Personal Injury, Legal Malpractice, Unlicensed Contractors, Medical Malpractice, Civil Litigation"
6. Contact information (i.e. contact number, website, and address) should be better positioned
7. Placement of endorsement logos should stand out more.
8. New picture of head attorney is attached.

Last but not least... Give it your best shot!

```html
<!DOCTYPE html>
<html lang="en">
<head>
<meta charset="utf-8">
<title>Marvolin Law Calendar Ad</title>
<link href="https://fonts.googleapis.com/css2?family=Montserrat:wght@500;600&family=Hind:wght@500;600;700&display=swap" rel="stylesheet">
<style>
  :root{
    --gold:#c9a46a;
    --gold-light:#d8bb8a;
    --gold-dark:#b8915a;
    --slate:#3f434b;
    --slate-dark:#34383f;
    --paper:#ffffff;
    --mist:#eeeeef;
    --stage:#d6d6d6;
    --ink:#2f3238;
  }
  html,body{margin:0;padding:0;width:900px;height:1200px;overflow:hidden;background:var(--stage);}
  .ad{
    position:absolute;left:20px;top:277px;width:860px;height:645px;
    background:var(--paper);overflow:hidden;
    box-shadow:0 10px 24px rgba(0,0,0,.25);
    font-family:"Hind",sans-serif;color:var(--ink);
  }
  .band-top{position:absolute;left:0;top:0;width:860px;height:186px;
    background:linear-gradient(120deg,var(--gold) 0%,var(--gold-light) 45%,var(--gold) 75%,var(--gold-dark) 100%);}
  .band-headline{position:absolute;left:0;top:186px;width:860px;height:107px;
    background:linear-gradient(100deg,#f7f7f7,var(--mist) 60%,#f9f9f9);}
  .band-practices{position:absolute;left:0;top:293px;width:860px;height:86px;
    background:linear-gradient(110deg,var(--gold-light),var(--gold) 55%,var(--gold-light));}
  .band-contact{position:absolute;left:0;top:379px;width:860px;height:144px;
    background:linear-gradient(100deg,#f4f4f4,#e9e9ea 50%,#f6f6f6);}
  .rule-gold{position:absolute;left:0;top:523px;width:860px;height:4px;background:var(--gold);}
  .footer{position:absolute;left:0;top:527px;width:860px;height:118px;background:var(--paper);}

  .brand-name{position:absolute;left:28px;top:92px;margin:0;
    font-family:"Montserrat",sans-serif;font-weight:500;font-size:50px;letter-spacing:5px;
    color:var(--paper);line-height:1;}
  .brand-tagline{position:absolute;left:143px;top:152px;margin:0;
    font-family:"Hind",sans-serif;font-weight:500;font-size:19px;letter-spacing:.6px;color:var(--paper);}

  .headline{position:absolute;left:30px;top:208px;margin:0;
    font-weight:700;font-size:31px;line-height:31px;letter-spacing:.6px;color:var(--slate);text-transform:uppercase;}
  .headline .accent{color:var(--gold);}

  .practices{position:absolute;left:20px;top:305px;width:520px;margin:0;padding:0;list-style:none;
    display:flex;flex-wrap:wrap;justify-content:center;row-gap:5px;column-gap:14px;}
  .practice{display:flex;align-items:center;gap:6px;color:var(--paper);font-weight:600;font-size:15.5px;line-height:26px;}
  .practice svg{width:16px;height:16px;}
  .practices .row-break{flex-basis:100%;height:0;}

  .tollfree-tab{position:absolute;left:188px;top:395px;width:132px;height:22px;background:var(--slate);
    color:var(--paper);font-weight:600;font-size:17px;line-height:24px;text-align:center;letter-spacing:.5px;}
  .phone-box{position:absolute;left:64px;top:414px;width:382px;height:64px;background:var(--slate);
    display:flex;align-items:center;justify-content:center;gap:14px;color:var(--paper);}
  .phone-box svg{width:38px;height:38px;}
  .phone-number{font-weight:600;font-size:42px;line-height:1;padding-top:6px;letter-spacing:.5px;}
  .website{position:absolute;left:148px;top:484px;width:212px;height:24px;background:var(--gold);
    display:flex;align-items:center;justify-content:center;gap:6px;color:var(--slate-dark);font-weight:500;font-size:15px;}
  .website svg{width:12px;height:12px;}

  .attorney-photo{position:absolute;left:540px;top:19px;width:300px;height:436px;
    background:linear-gradient(180deg,rgba(120,124,132,.55) 0%,rgba(110,114,122,.85) 45%,#5b5f67 100%);}
  .name-banner{position:absolute;left:492px;top:455px;width:368px;height:63px;background:var(--slate);
    clip-path:polygon(28px 0,100% 0,100% 100%,0 100%);}
  .attorney-name{position:absolute;left:500px;top:455px;width:352px;height:63px;margin:0;
    display:flex;align-items:center;justify-content:center;padding-top:6px;box-sizing:border-box;
    color:var(--gold);font-weight:600;font-size:26px;letter-spacing:.4px;}

  .address{position:absolute;left:28px;top:563px;display:flex;gap:8px;font-style:normal;font-size:14.5px;line-height:20px;color:var(--ink);}
  .address svg{width:14px;height:14px;margin-top:2px;}
  .footer-divider{position:absolute;left:291px;top:539px;width:1px;height:92px;background:#8a8d93;}
  .badge{position:absolute;}
  .badge-accredited{left:320px;top:562px;width:90px;height:36px;border-radius:4px;background:#1f5a96;}
  .badge-seal{left:438px;top:547px;width:66px;height:66px;border-radius:50%;background:#7a1d1d;}
  .badge-rating{left:542px;top:549px;width:66px;height:66px;border-radius:50%;background:#3a9fd8;}
  .badge-reviews{left:644px;top:562px;width:80px;height:46px;border-radius:3px;background:#d32323;}
  .badge-listing{left:750px;top:549px;width:84px;height:60px;border-radius:3px;background:var(--gold-dark);}
</style>
</head>
<body>
<main class="ad">
  <div class="band-top"></div>
  <div class="band-headline"></div>
  <div class="band-practices"></div>
  <div class="band-contact"></div>
  <div class="rule-gold"></div>
  <div class="footer"></div>

  <h1 class="brand-name">MARVOLIN LAW</h1>
  <p class="brand-tagline">SHAPING FAITH WITH RESULTS</p>

  <h2 class="headline">Known and trusted in our<br>community for over <span class="accent">22 years</span></h2>

  <ul class="practices">
    <li class="practice"><svg viewBox="0 0 16 16"><circle cx="8" cy="4.5" r="3.2" fill="#fff"/><path d="M2 15c0-4 2.7-6 6-6s6 2 6 6z" fill="#fff"/></svg>Personal Injury</li>
    <li class="practice"><svg viewBox="0 0 16 16"><path d="M8 1v13M3 4h10M1 9l2-5 2 5zM11 9l2-5 2 5zM5 14h6" stroke="#fff" stroke-width="1.3" fill="none"/></svg>Legal Malpractice</li>
    <li class="practice"><svg viewBox="0 0 16 16"><path d="M3 6a5 5 0 0110 0z" fill="#fff"/><rect x="2" y="6" width="12" height="1.6" fill="#fff"/><path d="M2 15c0-4 2.7-5.5 6-5.5s6 1.5 6 5.5z" fill="#fff"/></svg>Unlicensed Contractors</li>
    <li class="row-break"></li>
    <li class="practice"><svg viewBox="0 0 16 16"><path d="M8 1v14M1 5c3 0 5 1 7 3 2-2 4-3 7-3" stroke="#fff" stroke-width="1.4" fill="none"/></svg>Medical Malpractice</li>
    <li class="practice"><svg viewBox="0 0 16 16"><circle cx="8" cy="8" r="6" fill="none" stroke="#fff" stroke-width="1.6"/><circle cx="8" cy="8" r="2.4" fill="#fff"/></svg>Civil Litigation</li>
  </ul>

  <div class="tollfree-tab">TOLL FREE:</div>
  <div class="phone-box">
    <svg viewBox="0 0 38 38"><circle cx="19" cy="19" r="16.5" fill="none" stroke="#fff" stroke-width="2.4"/><path d="M13 11c1-1 2.2-1 3 0l2 3c.5.8.3 1.6-.4 2.2l-1.2 1c1 2 2.4 3.4 4.4 4.4l1-1.2c.6-.7 1.4-.9 2.2-.4l3 2c1 .8 1 2 0 3l-1.3 1.3c-1.4 1.4-4 1-7-1.2-3-2.2-5.6-5-7-8-1.2-2.6-1.4-4.6 0-6z" fill="#fff"/></svg>
    <span class="phone-number">(800) 412-7730</span>
  </div>
  <div class="website">
    <svg viewBox="0 0 12 12"><circle cx="6" cy="6" r="5" fill="none" stroke="#34383f" stroke-width="1.2"/><path d="M1 6h10M6 1c-2.5 3-2.5 7 0 10M6 1c2.5 3 2.5 7 0 10" stroke="#34383f" stroke-width="1" fill="none"/></svg>
    www.marvolinlegal.com
  </div>

  <div class="attorney-photo" role="img" aria-label="Portrait photo of attorney Gordon R. Marvolin in a grey suit"></div>
  <div class="name-banner"></div>
  <p class="attorney-name">Gordon R. Marvolin, Esq.</p>

  <address class="address">
    <svg viewBox="0 0 14 14"><path d="M7 1a4 4 0 014 4c0 3-4 8-4 8S3 8 3 5a4 4 0 014-4z" fill="none" stroke="#2f3238" stroke-width="1.2"/><circle cx="7" cy="5" r="1.4" fill="#2f3238"/></svg>
    <span>2210 Larkspur Ave., Suite #508<br>Westmere Hills, CA 90377</span>
  </address>
  <div class="footer-divider"></div>

  <div class="badge badge-accredited" role="img" aria-label="Business accreditation badge"></div>
  <div class="badge badge-seal" role="img" aria-label="Professional membership seal"></div>
  <div class="badge badge-rating" role="img" aria-label="Attorney rating badge"></div>
  <div class="badge badge-reviews" role="img" aria-label="Customer reviews badge"></div>
  <div class="badge badge-listing" role="img" aria-label="Lawyer directory listing badge"></div>
</main>
</body>
</html>
```